Thornbury Ridge & Beam Consultants- WEB DESIGN

I am seeking a more professional face to my current website.

www.TRBconsultants.com.au

Using same pages and same text, i need the pages to be presented in a more professional manner.

Use Same logo however all other items may be changed to make it look better... Main theme being a navy blue.

Project Deadline Extended
Reason: Alot of recent interest. Awaiting designs.

Target Market(s)

Engineers, Students, Public, Local Authorities, Draftsmen, Architects, Builders etc

Requirements
Must have
• Logo as per site,
• Navy Blue Theme,
• Professional feel,
• Images to attract eye and clients attention. (dont use large infrastructure yet more Residential designs, Crack inspections and Residential Construction)

```html
<!DOCTYPE html>
<html lang="en">
<head>
<meta charset="utf-8">
<title>Thornbury Ridge &amp; Beam Consultants</title>
<link href="https://fonts.googleapis.com/css2?family=Source+Sans+3:wght@400;600;700&display=swap" rel="stylesheet">
<style>
:root{
  --navy:#2b3a98;
  --navy-dark:#1f2c7c;
  --navy-light:#4355b8;
  --orange:#e39a1f;
  --black-btn:#222;
  --text:#333;
  --text-soft:#555;
  --card-grey:#e6e5e3;
  --line:#c9c9c9;
  --white:#fff;
}
*{margin:0;padding:0;box-sizing:border-box}
html,body{width:1013px;height:1200px;overflow:hidden;background:var(--white)}
body{position:relative;font-family:"Source Sans 3",Arial,sans-serif;color:var(--text)}
.abs{position:absolute}

/* header */
.brand{left:72px;top:40px;display:flex;align-items:center;gap:12px}
.brand-mark{width:40px;height:40px;background:var(--navy)}
.brand-name{color:var(--navy);font-weight:700;font-size:17px;line-height:20px;letter-spacing:2px;text-transform:uppercase}
.btn{display:block;height:29px;line-height:29px;border-radius:3px;color:var(--white);font-size:12px;text-align:center}
.btn-login{left:767px;top:17px;width:59px;background:var(--orange)}
.btn-register{left:847px;top:17px;width:72px;background:var(--black-btn)}
.search{left:730px;top:75px;width:189px;height:29px;border:1px solid var(--line);border-radius:3px;font-size:11px;font-style:italic;color:#999;padding:7px 5px}
.search svg{position:absolute;right:9px;top:7px}

/* nav */
.nav{left:0;top:125px;width:1013px;height:40px;background:linear-gradient(#4353b4,var(--navy) 60%,var(--navy-dark));border-top:1px solid #1a266e;display:flex;padding-left:66px}
.nav a{color:var(--white);font-size:14px;line-height:40px;text-align:center;text-decoration:none;border-right:1px solid #5a6bc8;text-transform:uppercase}
.nav a:last-child{border-right:none}

/* hero */
.hero{left:0;top:165px;width:1013px;height:366px;background:linear-gradient(100deg,#cfcfcd 0%,#e8e8e6 25%,#f0c419 40%,#e6b40c 55%,#dcdcda 68%,#c9c9c7 100%)}
.reg-form{left:85px;top:180px;width:231px;height:322px;background:rgba(70,60,30,.72);border:1px solid rgba(255,255,255,.25);padding:14px 12px}
.reg-form h2{color:var(--white);font-size:14px;font-weight:600;margin-bottom:12px}
.field{background:var(--white);border-radius:3px;height:29px;font-size:11px;color:#444;padding:7px 6px;margin-bottom:12px}
.reg-form label{display:block;color:var(--white);font-size:13px;font-weight:600;margin:-2px 0 6px 2px}
.select{width:96px;display:flex;justify-content:space-between;align-items:center}
.select span.arrow{width:16px;height:16px;background:#ddd;border:1px solid #aaa;display:flex;align-items:center;justify-content:center}
.reg-submit{position:absolute;right:22px;bottom:14px;width:76px;height:27px;background:var(--orange);color:var(--white);font-size:13px;text-align:center;line-height:27px}
.slider-arrows{left:893px;top:481px;display:flex;gap:1px}
.slider-arrows span{width:17px;height:22px;background:rgba(60,60,60,.75);display:flex;align-items:center;justify-content:center}

/* service cards */
.card{top:566px;width:191px;height:208px;background:var(--card-grey);border-radius:7px;padding:10px 7px}
.card.active{background:var(--navy)}
.card-img{width:177px;height:126px}
.card h3{font-size:13px;font-weight:600;color:#222;margin:8px 0 4px;text-transform:uppercase}
.card h3.small{font-size:11.5px}
.card p{font-size:11.5px;line-height:18px;color:var(--text-soft)}
.card.active h3,.card.active p{color:var(--white)}

/* content */
.welcome{left:81px;top:818px;width:550px}
.welcome h1,.offers h2{font-size:18px;font-weight:400;color:#111;margin-bottom:14px}
.welcome h4{font-size:13px;font-weight:400;text-transform:uppercase;color:#333;margin-bottom:10px}
.welcome p{font-size:11.5px;line-height:19.5px;color:var(--text-soft);margin-bottom:4px}
.offers{left:661px;top:818px;width:258px}
.offers h2{margin-bottom:12px}
.offer-img{width:259px;height:100px;background:linear-gradient(90deg,#c4cfd8,#8fb0c8 50%,#7fa05a 80%,#c9b23b)}
.offers p{font-size:11.5px;line-height:22px;color:#333;margin-top:6px}

/* footer */
.footer-shadow{left:80px;top:1054px;width:840px;height:22px;background:radial-gradient(ellipse at top,rgba(0,0,0,.22),rgba(0,0,0,0) 70%)}
.footer-links{left:72px;top:1097px;font-size:11.5px;color:#333}
.copy{left:73px;top:1131px;font-size:11.5px;color:#333}
.badge{top:1097px}
.badge-a{left:465px;width:40px;height:59px;background:#1b7fd6}
.badge-b{left:535px;top:1102px;width:46px;height:54px;background:#d71920}
.badge-c{left:598px;top:1100px;width:192px;height:52px;border-radius:26px;background:#2b3f7e}
.social{left:821px;top:1116px;display:flex;gap:12px}
.social span{width:23px;height:23px;border-radius:50%;background:#8a8a8a}
</style>
</head>
<body>

<header>
  <div class="abs brand">
    <div class="brand-mark"></div>
    <div class="brand-name">Thornbury Ridge &amp; Beam<br>Consultants</div>
  </div>
  <a class="abs btn btn-login">LOGIN</a>
  <a class="abs btn btn-register">REGISTER</a>
  <div class="abs search">Search..
    <svg width="12" height="12" viewBox="0 0 12 12"><circle cx="5" cy="5" r="3.8" fill="none" stroke="#999" stroke-width="1.6"/><line x1="8" y1="8" x2="11" y2="11" stroke="#999" stroke-width="1.8"/></svg>
  </div>
</header>

<nav class="abs nav">
  <a style="width:93px">Home</a>
  <a style="width:120px">Products</a>
  <a style="width:108px">Services</a>
  <a style="width:107px">Quality</a>
  <a style="width:90px">News</a>
  <a style="width:123px">Reference</a>
  <a style="width:111px">Register</a>
  <a style="width:115px">Contact</a>
</nav>

<div class="abs hero" role="img" aria-label="Yellow hard hat resting on engineering plans with pens and drafting tools"></div>

<form class="abs reg-form">
  <h2>REGISTRATION FORM</h2>
  <div class="field">Business Name</div>
  <div class="field">Suburb</div>
  <label>State</label>
  <div class="field select">VIC <span class="arrow"><svg width="7" height="4"><path d="M0 0h7L3.5 4z" fill="#333"/></svg></span></div>
  <div class="field">Your Name</div>
  <div class="field">Phone</div>
  <div class="reg-submit">REGISTER</div>
</form>

<div class="abs slider-arrows">
  <span><svg width="7" height="11"><path d="M6 1L1 5.5 6 10" fill="none" stroke="#fff" stroke-width="1.5"/></svg></span>
  <span><svg width="7" height="11"><path d="M1 1l5 4.5L1 10" fill="none" stroke="#fff" stroke-width="1.5"/></svg></span>
</div>

<section>
  <div class="abs card active" style="left:80px">
    <div class="card-img" role="img" aria-label="Curved glass office building against the sky" style="background:linear-gradient(#aeb8d8,#6f86a8 60%,#3e5373)"></div>
    <h3>Structural Engineering</h3>
    <p>Sedianommy nibh euismode loren tincidunt laores.</p>
  </div>
  <div class="abs card" style="left:297px">
    <div class="card-img" role="img" aria-label="Red house beside an energy rating scale" style="background:linear-gradient(90deg,#8fc46a,#f1c232 30%,#f3f3f3 45%,#d62b2b 75%,#f3f3f3)"></div>
    <h3>Energy Rating</h3>
    <p>Sedianommy nibh euismode loren tincidunt laores.</p>
  </div>
  <div class="abs card" style="left:513px">
    <div class="card-img" role="img" aria-label="Model house with keys on an inspection report" style="background:linear-gradient(#f2f2f2,#6e8c7a 45%,#eeeeee 75%,#d9d2cc)"></div>
    <h3 class="small">House Inspections</h3>
    <p>Sedianommy nibh euismode loren tincidunt laores.</p>
  </div>
  <div class="abs card" style="left:728px">
    <div class="card-img" role="img" aria-label="Workers tying steel reinforcement on a construction site" style="background:linear-gradient(#c9d3dc,#9a8060 55%,#6b4c32)"></div>
    <h3 class="small">Construction</h3>
    <p>Sedianommy nibh euismode loren tincidunt laores.</p>
  </div>
</section>

<section class="abs welcome">
  <h1>Welcome to Our Website</h1>
  <h4>Tempor incididunt ut labore et dolore magna aliqua. Ut enim ad minim veniam</h4>
  <p>Incididunt ut labore et dolore magna aliqua. Ut enim ad minim veniam, quis nostrud exercitation ullamco laboris nisi ut aliquip ex ea commodo consequat. Duis tefd&nbsp; aute irure dolor in reprehenderit in voluptate velit esse cillum.</p>
  <p>Dolore magna aliqua. Ut enim ad minim veniam, quis nostrud exercitation ullamco laboris nisi ut aliquip ex ea commodo consequat. Duis aute irure dolor in reprehenderit in voluptate velit esse&nbsp; cillum dolore eu fugiat nul a pariatur. Excepteur sint occaecat cupidatat non proident.</p>
</section>

<aside class="abs offers">
  <h2>Special Offers</h2>
  <div class="offer-img" role="img" aria-label="Special offer stamp beside a surveying level on a tripod"></div>
  <p>Nunc venenatis lacinia lacus quis vulputate. Sus pendisse imperdiet leo sed urna molestie.</p>
</aside>

<footer>
  <div class="abs footer-shadow"></div>
  <div class="abs footer-links">Home | Products | Services | Quality | News | Reference | Register | Contact</div>
  <div class="abs copy">© 2013 Copyrights Reserved. All rights reserved.</div>
  <div class="abs badge badge-a"></div>
  <div class="abs badge badge-b"></div>
  <div class="abs badge badge-c"></div>
  <div class="abs social"><span></span><span></span><span></span></div>
</footer>

</body>
</html>
```